Small company security and risk consulting startup needs an explosive message via marketing colla...

Need a two page (front/back) flyer that calls out our three primary service areas incorporating brandmill developed logo and website visuals. Something that grabs attention at first glance to entice the viewer to read and connect for a services consultation. I will need the ability to make minor adjustments and add language.

```html
<!DOCTYPE html>
<html lang="en">
<head>
<meta charset="utf-8">
<title>Vantage Shield Consulting Services – Flyer</title>
<link rel="stylesheet" href="https://fonts.googleapis.com/css2?family=Anton&family=Bebas+Neue&family=Lato:ital,wght@0,300;0,400;0,700;0,900;1,900&display=swap">
<style>
  :root {
    --navy: #0c2431;
    --navy-deep: #0a1b24;
    --red: #ed1c24;
    --red-dark: #5a0f12;
    --yellow: #fff200;
    --white: #ffffff;
    --grey-edge: #7d7d7d;
    --grey-mid: #f4f4f4;
  }
  * { margin: 0; padding: 0; box-sizing: border-box; }
  html, body { width: 1200px; height: 2902px; overflow: hidden; }
  body {
    position: relative;
    background: radial-gradient(ellipse 60% 50% at 50% 50%, var(--grey-mid) 0%, #cfcfcf 55%, var(--grey-edge) 100%);
    font-family: "Lato", sans-serif;
    color: var(--white);
  }
  .page { position: absolute; left: 127px; width: 947px; height: 1339px; overflow: hidden; }
  .page-front { top: 68px; background: var(--navy); }
  .page-back { top: 1475px; }
  .shapes { position: absolute; inset: 0; }
  .abs { position: absolute; }

  .title-word {
    font-family: "Anton", sans-serif;
    font-size: 116px; line-height: 1; letter-spacing: 2px;
    color: var(--white);
  }
  .title-sub {
    font-family: "Lato", sans-serif; font-weight: 900; font-style: italic;
    font-size: 41px; color: var(--yellow); white-space: nowrap; letter-spacing: 0.5px;
  }
  .brand-name { font-family: "Lato", sans-serif; font-weight: 900; font-size: 38px; color: var(--red); white-space: nowrap; }
  .brand-sub { font-size: 15px; font-weight: 700; letter-spacing: 6px; white-space: nowrap; }
  .brand-tag { font-size: 11px; font-weight: 700; letter-spacing: 3.5px; color: var(--red); white-space: nowrap; }

  .section-head {
    font-weight: 700; font-size: 48px; line-height: 1; white-space: nowrap;
    padding-bottom: 8px; border-bottom: 4px solid var(--red);
  }
  .body-copy { font-weight: 300; font-size: 15.5px; line-height: 19px; }

  .service-head { font-family: "Bebas Neue", sans-serif; font-size: 49px; line-height: 56px; white-space: nowrap; }
  .service-copy { font-weight: 300; font-size: 15.5px; line-height: 19px; width: 310px; }

  .contact-head { font-size: 44px; font-weight: 700; color: var(--yellow); white-space: nowrap; line-height: 1; }
  .contact-line { font-size: 32px; font-weight: 400; white-space: nowrap; line-height: 1; }
  .follow-label { font-size: 24px; font-weight: 700; white-space: nowrap; }
</style>
</head>
<body>

<section class="page page-front">
  <svg class="shapes" width="947" height="1339" viewBox="0 0 947 1339">
    <defs>
      <radialGradient id="hero-tone" cx="0.6" cy="0.45" r="0.7">
        <stop offset="0" stop-color="#b3181e"/>
        <stop offset="0.55" stop-color="#5e1116"/>
        <stop offset="1" stop-color="#2a0b0e"/>
      </radialGradient>
    </defs>
    <polygon points="0,0 947,0 947,631 0,316" fill="url(#hero-tone)" role="img" aria-label="Close-up of an eye overlaid with digital scanning graphics"/>
    <polygon points="515,604 947,834 947,1339 515,1339" fill="var(--red)"/>
    <rect x="0" y="700" width="515" height="639" fill="var(--navy-deep)" opacity="0.35"/>
  </svg>

  <div class="abs title-word" style="left:457px; top:140px;">VANTAGE</div>
  <div class="abs title-word" style="left:482px; top:272px;">SHIELD</div>
  <div class="abs title-sub" style="left:467px; top:373px;">CONSULTING SERVICES</div>

  <svg class="abs" style="left:216px; top:500px;" width="40" height="40" viewBox="0 0 40 40"><rect x="2" y="2" width="36" height="36" fill="var(--red)"/></svg>
  <div class="abs brand-name" style="left:70px; top:536px;">VantageShield</div>
  <div class="abs brand-sub" style="left:104px; top:577px;">CONSULTING SERVICES</div>
  <div class="abs brand-tag" style="left:118px; top:598px;">commitment - integrity - results</div>

  <h2 class="abs section-head" style="left:48px; top:741px; width:240px;">ABOUT US</h2>
  <p class="abs body-copy" style="left:52px; top:807px; width:365px;">Lorem ipsum dolor sit amet, consectetuer adipiscing elit, sed diam nonummy nibh euismod tincidunt ut laoreet dolore magna aliquam erat volutpat. Ut wisi enim ad minim veniam, quis nostrud exerci tation ullamcorper suscipit lobortis nisl ut aliquip ex ea commodo consequat. Duis autem vel eum iriure dolor in hendrerit in vulputate velit esse molestie consequat, vel illum dolore eu feugiat nulla facilisis at</p>

  <h2 class="abs section-head" style="left:48px; top:1030px; width:317px;">WHY&nbsp; WE ARE</h2>
  <p class="abs body-copy" style="left:52px; top:1088px; width:365px;">Lorem ipsum dolor sit amet, consectetuer adipiscing elit, sed diam nonummy nibh euismod tincidunt ut laoreet dolore magna aliquam erat volutpat. Ut wisi enim ad minim veniam, quis nostrud exerci tation ullamcorper suscipit lobortis nisl ut aliquip ex ea commodo consequat. Duis autem vel eum iriure dolor in hendrerit in vulputate velit esse molestie</p>

  <svg class="shapes" width="947" height="1339" viewBox="0 0 947 1339" fill="none" stroke="#111" stroke-width="3" stroke-linecap="round" stroke-linejoin="round">
    <g class="service-badge">
      <circle cx="491" cy="863" r="63" fill="var(--red)" stroke="none"/>
      <circle cx="491" cy="859" r="63" fill="var(--white)" stroke="none"/>
      <rect x="458" y="833" width="66" height="46" rx="3"/>
      <path d="M480 891 h22 M491 879 v12 M466 841 v-4 h6 M516 841 v-4 h-6 M466 871 v4 h6 M516 871 v4 h-6"/>
      <path d="M474 856 q17 -14 34 0 q-17 14 -34 0z"/>
      <circle cx="491" cy="856" r="4"/>
    </g>
    <g class="service-badge">
      <circle cx="491" cy="1044" r="63" fill="var(--red)" stroke="none"/>
      <circle cx="491" cy="1040" r="63" fill="var(--white)" stroke="none"/>
      <path d="M470 1075 v-14 q-14 -8 -12 -26 q3 -22 30 -24 q26 0 30 22 l5 12 h-6 v12 h-12 v18"/>
      <circle cx="491" cy="1036" r="11"/>
      <circle cx="491" cy="1036" r="4"/>
      <path d="M458 1030 h-12 M454 1050 h-10 M520 1022 l10 -8"/>
    </g>
    <g class="service-badge">
      <circle cx="491" cy="1224" r="63" fill="var(--red)" stroke="none"/>
      <circle cx="491" cy="1220" r="63" fill="var(--white)" stroke="none"/>
      <path d="M478 1240 v-8 q-14 -10 -14 -26 q0 -26 27 -26 q27 0 27 26 q0 16 -14 26 v8z"/>
      <path d="M480 1247 h22 M483 1254 h16"/>
      <rect x="462" y="1186" width="26" height="20" fill="var(--white)"/>
      <rect x="496" y="1198" width="30" height="22" fill="var(--white)"/>
      <path d="M467 1193 h16 M467 1199 h12 M501 1205 h20 M501 1211 h14"/>
    </g>
  </svg>

  <h3 class="abs service-head" style="left:569px; top:820px;">NATIONAL SECURITY</h3>
  <p class="abs service-copy" style="left:569px; top:869px;">Lorem ipsum dolor sit amet, consectetuer adipiscing elit, sed diam nonummy nibh euismod tincidunt ut laoreet dolore magna aliquam erat</p>

  <h3 class="abs service-head" style="left:569px; top:982px;">RISK MANAGEMENT<br>SERVICES</h3>
  <p class="abs service-copy" style="left:569px; top:1087px;">Lorem ipsum dolor sit amet, consectetuer adipiscing elit, sed diam nonummy nibh euismod tincidunt ut laoreet dolore magna aliquam erat</p>

  <h3 class="abs service-head" style="left:569px; top:1183px;">CONSULTING SERVICES</h3>
  <p class="abs service-copy" style="left:569px; top:1237px;">Lorem ipsum dolor sit amet, consectetuer adipiscing elit, sed diam nonummy nibh euismod tincidunt ut laoreet dolore magna aliquam erat</p>
</section>

<section class="page page-back">
  <svg class="shapes" width="947" height="1339" viewBox="0 0 947 1339">
    <defs>
      <linearGradient id="back-base" x1="0" y1="0" x2="0" y2="1">
        <stop offset="0" stop-color="#e0262c"/>
        <stop offset="0.45" stop-color="#c41d23"/>
        <stop offset="1" stop-color="#8e1318"/>
      </linearGradient>
      <radialGradient id="back-shadow" cx="0.2" cy="0.55" r="0.45">
        <stop offset="0" stop-color="#2a080a" stop-opacity="0.85"/>
        <stop offset="1" stop-color="#2a080a" stop-opacity="0"/>
      </radialGradient>
      <radialGradient id="back-glow" cx="0.75" cy="0.62" r="0.35">
        <stop offset="0" stop-color="#f03a3f" stop-opacity="0.7"/>
        <stop offset="1" stop-color="#f03a3f" stop-opacity="0"/>
      </radialGradient>
    </defs>
    <g role="img" aria-label="Analyst seated at a desk watching security monitoring screens, red duotone">
      <rect width="947" height="1339" fill="url(#back-base)"/>
      <rect width="947" height="1339" fill="url(#back-shadow)"/>
      <rect width="947" height="1339" fill="url(#back-glow)"/>
    </g>
    <rect x="0" y="1154" width="947" height="166" fill="var(--navy)"/>
    <rect x="0" y="1320" width="947" height="19" fill="#3a0a0d"/>
  </svg>

  <div class="abs contact-head" style="left:56px; top:1117px;">GET IN TOUCH</div>

  <svg class="abs" style="left:30px; top:1174px;" width="28" height="28" viewBox="0 0 24 24" fill="var(--white)"><path d="M12 2a7 7 0 0 0-7 7c0 5 7 13 7 13s7-8 7-13a7 7 0 0 0-7-7zm0 9.5a2.5 2.5 0 1 1 0-5 2.5 2.5 0 0 1 0 5z"/></svg>
  <div class="abs contact-line" style="left:81px; top:1172px;">482 Harlow Avenue Suite 12 Austin TX 78701</div>

  <svg class="abs" style="left:28px; top:1220px;" width="30" height="30" viewBox="0 0 24 24" fill="var(--white)"><path d="M6.6 10.8a15 15 0 0 0 6.6 6.6l2.2-2.2a1 1 0 0 1 1-.25 11.4 11.4 0 0 0 3.6.57 1 1 0 0 1 1 1V20a1 1 0 0 1-1 1A17 17 0 0 1 3 4a1 1 0 0 1 1-1h3.5a1 1 0 0 1 1 1c0 1.25.2 2.45.57 3.6a1 1 0 0 1-.25 1z"/></svg>
  <div class="abs contact-line" style="left:81px; top:1218px;">(555) 014 2287</div>

  <svg class="abs" style="left:28px; top:1271px;" width="30" height="24" viewBox="0 0 30 24" fill="none" stroke="var(--white)" stroke-width="2.5"><rect x="2" y="3" width="26" height="18"/><path d="M2 3l13 10 13-10M2 21l10-9M28 21l-10-9"/></svg>
  <div class="abs contact-line" style="left:81px; top:1265px;">hello@vantageshield.com</div>

  <div class="abs follow-label" style="left:750px; top:1244px;">FOLLOW US</div>
  <svg class="abs" style="left:755px; top:1268px;" width="140" height="30" viewBox="0 0 140 30" fill="var(--white)">
    <circle cx="15" cy="15" r="13"/>
    <circle cx="63" cy="15" r="13"/>
    <circle cx="112" cy="15" r="13"/>
  </svg>
</section>

</body>
</html>
```